Stage Design Company Business Card

We are looking to step up up our business card design for our team.

We are a Full service Design and Consultation company for Stage and TV with an emphasis in Theatrical Lighting.

We like our materials to be clean and modern with solid colors free of patterns and gradients. Our brand consists of 4 primary colors Purple, Black, Grey, and White. Provided is our Word Mark as well as our Symbol Logo.

We would like our cards to leave an impression beyond the information, show our attention to design and detail, and make our marks an easily recognized feature (together or apart) for our clients.

We need a warm approachable comfortable feel for some clients, and a professional flair for the board member type clients.

Attached are our brand elements, and our existing cards to give a sense of our style and a glipse at the information we provide on our cards.

Target Market(s)

broad client base from church leaders to high school teachers and architects.

Industry/Entity Type

Business

Contact Information for Business Card

We format our phone number with periods not parenthesis or dashes. Information will be edited for each of our team members, and team member specific cards are not part of this scope, but rather a template so to speak.

Font styles to use
Sans Serif

Colors
6b449b
ffffff
000000
333333
aaaaaa

Requirements
Must have
• Wordmark and logo mark present (does not need to exist on the same side of card)
• Brand Colors,
• Name, Phone, Email, Address.
• Unique choices that make someone stop and take a second look
Nice to have
• It would be nice to somehow convey what we DO, as our brand name does not lend itself to this, outside of an obvious tagline though.....
• social media if not crowded. all of our handles match (instagram, twitter, facebook)
Should not have
• "clipart"

```html
<!DOCTYPE html>
<html lang="en">
<head>
<meta charset="utf-8">
<title>Marlow Stageworks — Business Card</title>
<link href="https://fonts.googleapis.com/css2?family=Questrial&display=swap" rel="stylesheet">
<style>
  :root {
    --stage-bg: #e8e3db;
    --brand-purple: #37236b;
    --brand-lilac: #c9c0e0;
    --card-white: #ffffff;
    --card-shadow: rgba(40, 30, 20, 0.22);
  }
  * { box-sizing: border-box; margin: 0; padding: 0; }
  html, body {
    width: 1200px;
    height: 995px;
    overflow: hidden;
  }
  body {
    background: var(--stage-bg);
    font-family: "Questrial", sans-serif;
    display: flex;
    align-items: center;
    justify-content: center;
    gap: 70px;
  }
  .card {
    width: 420px;
    height: 590px;
    flex-shrink: 0;
    border-radius: 26px;
    box-shadow: 0 8px 24px var(--card-shadow);
    display: flex;
    flex-direction: column;
    align-items: center;
    text-align: center;
  }

  /* Front */
  .card-front {
    background: var(--brand-purple);
    color: var(--card-white);
    padding-top: 150px;
  }
  .brand-mark {
    width: 96px;
    height: 96px;
    flex-shrink: 0;
    border-radius: 50%;
    background: var(--card-white);
  }
  .brand-name {
    margin-top: 44px;
    font-size: 28px;
    letter-spacing: 0.14em;
    white-space: nowrap;
    color: var(--card-white);
  }
  .brand-url {
    margin-top: 20px;
    font-size: 18px;
    letter-spacing: 0.28em;
    white-space: nowrap;
    color: var(--brand-lilac);
  }

  /* Back */
  .card-back {
    background: var(--card-white);
    color: var(--brand-purple);
    padding-top: 150px;
  }
  .member-name {
    font-size: 32px;
    font-weight: 400;
    letter-spacing: 0.06em;
    white-space: nowrap;
  }
  .contact-block,
  .address-block {
    font-size: 24px;
    line-height: 1.2;
    letter-spacing: 0.03em;
    white-space: nowrap;
  }
  .contact-block { margin-top: 34px; }
  .address-block { margin-top: 36px; }
</style>
</head>
<body>
  <section class="card card-front">
    <span class="brand-mark" aria-hidden="true"></span>
    <p class="brand-name">MARLOW STAGEWORKS</p>
    <p class="brand-url">MARLOW-SW.COM</p>
  </section>

  <section class="card card-back">
    <h1 class="member-name">DANA R HOLLIS</h1>
    <p class="contact-block">555.014.7730<br>dana@marlow-sw.com</p>
    <p class="address-block">120 N ELM AVE<br>FAIRBROOK, AZ 85099</p>
  </section>
</body>
</html>
```